Motivational Poster Design Project

I would like to create a poster with some of my favorite Quotewell to hang in my office.

Industry/Entity Type

Quotewell

Requirements
Must have
• The poster will be 24" high x 36" long and printed on canvas, so the image you create needs to have a resolution of at least 2700 x 3900.

The poster must contain the following Quotewell:

“Your beliefs become your thoughts,
Your thoughts become your words,
Your words become your actions,
Your actions become your habits,
Your habits become your values,
Your values become your destiny.”
-Varuna Pellath

"Winners practice until they get it right. Champions practice until they can’t get it wrong!"
-Unknown

"Style is the perfection of a point of view."
-Conrad Whitlowe

"My interest in life comes from setting myself huge, apparently unachieveable challenges and trying to rise above them."
-Sir Oswin Talbrook

"Problems cannot be solved by the same level of thinking that created them."
-Gustav Morrendel

"People think focus means saying yes to the thing you've got to focus on. But that's not what it means at all. It means saying no to the hundred other good ideas that there are. You have to pick carefully."
-Dale Parrick

"Think like a man of action and act like a man of thought."
-Lucien Marvaud
Nice to have
• It would be nice to have an image of each person who is being quoted (if known) along with the quote that is attributable to them.

```html
<!DOCTYPE html>
<html lang="en">
<head>
<meta charset="utf-8">
<title>Quotewell – Top Quotes</title>
<link href="https://fonts.googleapis.com/css2?family=Arimo:wght@400;700&display=swap" rel="stylesheet">
<style>
  :root {
    --header-blue: #5b9fc2;
    --nav-navy: #2b5b7d;
    --nav-text: #9cc6de;
    --link-blue: #2a76ad;
    --ink: #111;
    --rule: #dfe5ea;
    --page-top: #ffffff;
    --page-mid: #eef3f7;
    --panel: #e9ecef;
    --panel-rule: #c9ced3;
    --ghost: #d3e0ec;
    --photo-light: #c9c9c9;
    --photo-dark: #3a3a3a;
  }
  * { box-sizing: border-box; margin: 0; padding: 0; }
  html, body { width: 800px; height: 1200px; overflow: hidden; }
  body {
    position: relative;
    font-family: "Arimo", Arial, sans-serif;
    color: var(--ink);
    background: radial-gradient(ellipse at 55% 40%, var(--page-top) 0%, var(--page-mid) 100%);
  }
  .site-header {
    position: absolute; left: 0; top: 0; width: 800px; height: 131px;
    background: var(--header-blue);
  }
  .brand {
    position: absolute; left: 46px; top: 46px;
    font-size: 44px; font-weight: 700; color: #fff; letter-spacing: -0.5px;
  }
  .tagline {
    position: absolute; left: 46px; top: 104px;
    font-size: 14px; font-weight: 700; color: #eaf4fa;
  }
  .search-label {
    position: absolute; left: 246px; top: 43px;
    font-size: 11px; color: #e6f1f7;
  }
  .search-box {
    position: absolute; left: 246px; top: 57px; width: 317px; height: 31px;
    background: #fff; border-radius: 2px;
  }
  .search-button {
    position: absolute; right: 2px; top: 2px; width: 105px; height: 27px;
    background: linear-gradient(#f4f6f8, #cdd5dc);
    border-radius: 2px; font-size: 20px; color: #222;
    display: flex; align-items: center; justify-content: center;
  }
  .account {
    position: absolute; right: 34px; top: 20px;
    display: flex; align-items: center; gap: 4px;
    font-size: 12px; color: #e6f1f7;
  }
  .sign-in {
    display: flex; align-items: center; gap: 5px;
    padding: 4px 6px; background: #7cb3d1; border-radius: 3px;
    font-weight: 700; color: #fff; font-size: 11px;
  }
  .main-nav {
    position: absolute; left: 0; top: 131px; width: 800px; height: 21px;
    background: var(--nav-navy);
    display: flex; align-items: center; gap: 7px; padding-left: 45px;
    font-size: 11px; color: var(--nav-text); white-space: nowrap;
  }
  .ghost-title {
    position: absolute; left: 137px; top: 793px;
    transform: translate(-50%, -50%) rotate(-90deg);
    font-size: 96px; color: var(--ghost); letter-spacing: 4px; white-space: nowrap;
  }
  .people-panel {
    position: absolute; left: 46px; top: 174px; width: 180px; height: 232px;
    background: var(--panel); border-radius: 4px;
  }
  .people-panel h2 {
    position: absolute; left: 13px; top: 12px;
    font-size: 11px; font-weight: 400;
  }
  .people-panel .rule {
    position: absolute; left: 13px; right: 13px; top: 32px; border-top: 1px solid var(--panel-rule);
  }
  .thumb { position: absolute; width: 43px; height: 55px; border: 2px solid #fff; }
  .panel-note {
    position: absolute; left: 67px; top: 188px; width: 105px;
    font-size: 7px; line-height: 1.35;
  }
  .quotes-head {
    position: absolute; left: 246px; top: 179px; width: 508px;
    display: flex; align-items: baseline; gap: 37px;
  }
  .quotes-head h1 { font-size: 21px; font-weight: 700; }
  .quotes-head a { font-size: 13px; color: var(--link-blue); text-decoration: none; }
  .quote-list {
    position: absolute; left: 246px; top: 207px; width: 508px;
    list-style: none; border-top: 1px solid var(--rule);
  }
  .quote-item {
    height: 136.3px; border-bottom: 1px solid var(--rule);
    display: flex; align-items: center; gap: 16px;
  }
  .portrait { flex: none; width: 72px; height: 91px; }
  .quote-text { font-size: 13px; line-height: 1.3; }
  .quote-text .name { font-size: 17.5px; font-weight: 700; color: var(--link-blue); }
  .quote-item.tall { align-items: flex-start; padding-top: 20px; }
  .quote-item.tall .quote-text { padding-top: 6px; }
</style>
</head>
<body>
  <header class="site-header">
    <div class="brand">Quotewell</div>
    <div class="tagline">Discover what’s a good words, for a good life</div>
    <div class="search-label">Search for a keyword or phrase...</div>
    <div class="search-box"><div class="search-button">Search</div></div>
    <div class="account">Have an account?
      <span class="sign-in">Sign in
        <svg width="14" height="14" viewBox="0 0 14 14"><circle cx="7" cy="7" r="6" fill="none" stroke="#fff" stroke-width="1.4"/><path d="M4 5.5 L7 8.8 L10 5.5 Z" fill="#fff"/></svg>
      </span>
    </div>
  </header>
  <nav class="main-nav">
    <span>Top Quotes</span><span>Top Quotes</span><span>Top Quotes</span><span>Top Quotes</span><span>Top Quotes</span><span>Top Quotes</span><span>Top Quotes</span><span>Top Quotes</span><span>Top Quotes</span><span>Top Quotes</span><span>Top Quotes</span>
  </nav>

  <div class="ghost-title">TOP QUOTES</div>

  <aside class="people-panel">
    <h2>See who’s here</h2>
    <div class="rule"></div>
    <div class="thumb" style="left:13px;top:39px;background:linear-gradient(#ddd,#999)" role="img" aria-label="Portrait of Varuna Pellath"></div>
    <div class="thumb" style="left:68px;top:39px;background:linear-gradient(#f2f2f2,#bbb)" role="img" aria-label="Silhouette for an unknown author"></div>
    <div class="thumb" style="left:123px;top:39px;background:linear-gradient(#bbb,#666)" role="img" aria-label="Portrait of Conrad Whitlowe"></div>
    <div class="thumb" style="left:13px;top:104px;background:linear-gradient(#eee,#555)" role="img" aria-label="Portrait of Sir Oswin Talbrook"></div>
    <div class="thumb" style="left:68px;top:104px;background:linear-gradient(#f4f4f4,#333)" role="img" aria-label="Portrait of Dale Parrick"></div>
    <div class="thumb" style="left:123px;top:104px;background:linear-gradient(#888,#333)" role="img" aria-label="Portrait of Gustav Morrendel"></div>
    <div class="thumb" style="left:13px;top:169px;background:linear-gradient(#aaa,#444)" role="img" aria-label="Portrait of Lucien Marvaud"></div>
    <p class="panel-note">Figures you watch. Peoples who inspire. Find it on Quotewell.</p>
  </aside>

  <div class="quotes-head"><h1>Top Quotes</h1><a href="#">View all &gt;</a></div>
  <ul class="quote-list">
    <li class="quote-item tall">
      <div class="portrait" style="background:linear-gradient(#e6e6e6,#8a8a8a)" role="img" aria-label="Portrait of Varuna Pellath"></div>
      <p class="quote-text"><span class="name">Varuna Pellath</span> : “Your beliefs become your thoughts, Your thoughts become your words, Your words become your actions, Your actions become your habits, Your habits become your values, Your values become your destiny.”</p>
    </li>
    <li class="quote-item">
      <div class="portrait" style="background:linear-gradient(#fafafa,#cfcfcf)" role="img" aria-label="Silhouette for an unknown author"></div>
      <p class="quote-text"><span class="name">Unknown</span> : "Winners practice until they get it right. Champions practice until they can’t get it wrong!"</p>
    </li>
    <li class="quote-item">
      <div class="portrait" style="background:linear-gradient(#b5b5b5,#5a5a5a)" role="img" aria-label="Portrait of Conrad Whitlowe"></div>
      <p class="quote-text"><span class="name">Conrad Whitlowe</span> : "Style is the perfection of a point of view."</p>
    </li>
    <li class="quote-item">
      <div class="portrait" style="background:linear-gradient(#f0f0f0,#3c3c3c)" role="img" aria-label="Portrait of Sir Oswin Talbrook"></div>
      <p class="quote-text"><span class="name">Sir Oswin Talbrook</span> : "My interest in life comes from setting myself huge, apparently unachieveable challenges and trying to rise above them."</p>
    </li>
    <li class="quote-item">
      <div class="portrait" style="background:linear-gradient(#7a7a7a,#2e2e2e)" role="img" aria-label="Portrait of Gustav Morrendel"></div>
      <p class="quote-text"><span class="name">Gustav Morrendel</span> : "Problems cannot be solved by the same level of thinking that created them."</p>
    </li>
    <li class="quote-item">
      <div class="portrait" style="background:linear-gradient(#f5f5f5,#2a2a2a)" role="img" aria-label="Portrait of Dale Parrick"></div>
      <p class="quote-text"><span class="name">Dale Parrick</span> : "People think focus means saying yes to the thing you've got to focus on. But that's not what it means at all. It means saying no to the hundred other good ideas that there are. You have to pick carefully."</p>
    </li>
    <li class="quote-item">
      <div class="portrait" style="background:linear-gradient(#a0a0a0,#3a3a3a)" role="img" aria-label="Portrait of Lucien Marvaud"></div>
      <p class="quote-text"><span class="name">Lucien Marvaud</span> : "Think like a man of action and act like a man of thought."</p>
    </li>
  </ul>
</body>
</html>
```